Therapy Department Recruitment Flyer

Recruitment flyer similar to nursing one attached but for Occupational Therapy and Physical Therapy. Please use pictures depicting therapy services being provided to elderly population.

```html
<!DOCTYPE html>
<html lang="en">
<head>
<meta charset="utf-8">
<title>Therapy Positions – Recruitment Flyer</title>
<link href="https://fonts.googleapis.com/css2?family=Roboto:wght@700;900&family=Roboto+Condensed:wght@400;700&display=swap" rel="stylesheet">
<style>
  :root {
    --stage: #243140;
    --blue: #0a6fb8;
    --deep-blue: #0b53a6;
    --green: #2a9136;
    --navy: #2a3648;
    --slate: #4a5562;
    --ink: #2b3440;
    --white: #ffffff;
  }
  * { box-sizing: border-box; margin: 0; padding: 0; }
  html, body { width: 1200px; height: 1200px; overflow: hidden; }
  body { background: var(--stage); position: relative; font-family: "Roboto Condensed", Arial, sans-serif; }

  .flyer {
    position: absolute; left: 213px; top: 100px;
    width: 773px; height: 1000px;
    background: var(--white); overflow: hidden;
  }
  .flyer-shapes { position: absolute; inset: 0; width: 773px; height: 1000px; }

  .badge {
    position: absolute; left: 34px; top: 20px; width: 140px; height: 140px;
    border-radius: 50%; background: var(--navy); border: 3px solid var(--white);
    display: flex; flex-direction: column; align-items: center; justify-content: center;
    padding: 0 18px;
    color: var(--white); font-weight: 700; font-size: 11px; line-height: 15px; text-align: center;
    white-space: nowrap;
  }

  .title-main, .title-sub, .title-org { position: absolute; white-space: nowrap; }
  .title-main { left: 38px; top: 186px; color: var(--blue); font-family: "Roboto", Arial, sans-serif; font-size: 62px; font-weight: 900; line-height: 62px; letter-spacing: -0.5px; }
  .title-sub { left: 43px; top: 245px; color: var(--blue); font-family: "Roboto", Arial, sans-serif; font-size: 40px; font-weight: 900; line-height: 42px; letter-spacing: 6px; }
  .title-org { left: 43px; top: 286px; color: var(--green); font-size: 25px; font-weight: 700; line-height: 30px; }

  .rate {
    position: absolute; left: 42px; width: 251px; height: 32px;
    border-radius: 16px; border: 2px solid; display: flex; overflow: hidden; background: var(--white);
  }
  .rate-role { width: 153px; color: var(--white); font-size: 16px; font-weight: 700; display: flex; align-items: center; justify-content: center; white-space: nowrap; }
  .rate-pay { flex: 1; font-size: 23px; font-weight: 700; display: flex; align-items: center; padding-left: 12px; }
  .rate--pt { top: 324px; border-color: var(--green); }
  .rate--pt .rate-role { background: var(--green); }
  .rate--pt .rate-pay { color: var(--green); }
  .rate--ot { top: 368px; border-color: var(--blue); }
  .rate--ot .rate-role { background: var(--blue); }
  .rate--ot .rate-pay { color: var(--blue); }

  .intro { position: absolute; right: 103px; top: 428px; width: 622px; text-align: right; }
  .intro-heading { color: var(--blue); font-size: 24px; font-weight: 700; line-height: 30px; margin-right: 3px; }
  .intro-body { color: var(--ink); font-size: 16.5px; line-height: 21px; margin-top: 9px; }
  .intro-rule { position: absolute; left: 697px; top: 431px; width: 3px; height: 123px; background: var(--blue); }

  .contact { position: absolute; right: 73px; top: 654px; text-align: right; color: var(--white); font-weight: 700; }
  .contact-title { font-size: 30px; line-height: 38px; margin-bottom: 4px; }
  .contact-line { font-size: 22px; line-height: 28px; }
  .contact-row { display: flex; align-items: center; justify-content: flex-end; gap: 12px; }
  .contact-phone { font-size: 22px; line-height: 30px; margin-top: 6px; }
  .contact-email { font-size: 14px; line-height: 22px; font-weight: 700; }
  .contact-row svg { flex: none; }
</style>
</head>
<body>
  <main class="flyer">
    <svg class="flyer-shapes" viewBox="0 0 1245 1610" preserveAspectRatio="none">
      <defs>
        <linearGradient id="gymTones" x1="0" y1="0" x2="1" y2="0.3">
          <stop offset="0" stop-color="#ffffff"/>
          <stop offset="0.4" stop-color="#e6eef0"/>
          <stop offset="0.65" stop-color="#c9dbc0"/>
          <stop offset="1" stop-color="#b8c2cc"/>
        </linearGradient>
        <linearGradient id="parkTones" x1="0" y1="0" x2="1" y2="1">
          <stop offset="0" stop-color="#8fae6a"/>
          <stop offset="0.5" stop-color="#c9cdd6"/>
          <stop offset="1" stop-color="#6d8a4c"/>
        </linearGradient>
        <linearGradient id="signTones" x1="0" y1="0" x2="0" y2="1">
          <stop offset="0" stop-color="#b9c6d6"/>
          <stop offset="0.5" stop-color="#5a5e64"/>
          <stop offset="1" stop-color="#a59c8e"/>
        </linearGradient>
      </defs>

      <rect role="img" aria-label="Photo: a therapist guiding an elderly woman through a floor exercise in a bright gym" x="0" y="0" width="1245" height="760" fill="url(#gymTones)"/>

      <path class="top-blob" d="M0 0 H720 C580 120 470 290 250 285 C140 282 60 265 0 250 Z" fill="var(--blue)"/>
      <path class="top-swoosh" d="M410 160 C520 60 630 12 740 0 H790 C650 22 520 80 410 160 Z" fill="var(--green)"/>

      <rect x="0" y="870" width="1245" height="740" fill="var(--deep-blue)"/>
      <rect role="img" aria-label="Photo: the care center's entrance sign with pine trees on a sunny day" x="640" y="1325" width="605" height="285" fill="url(#signTones)"/>

      <path class="wave-green" d="M0 650 C250 720 650 650 900 600 C1050 575 1150 590 1245 610 V900 H0 Z" fill="var(--green)"/>
      <path class="wave-blue" d="M0 682 C250 748 650 676 900 616 C1050 590 1150 606 1245 640 V900 H0 Z" fill="var(--blue)"/>
      <path class="wave-slate" d="M0 720 C250 790 650 720 900 640 C1050 605 1150 620 1245 680 V912 C1000 1045 700 1060 420 1000 C250 970 100 940 0 925 Z" fill="var(--slate)"/>
      <path class="panel-white" d="M0 705 C250 790 650 720 900 640 C1050 605 1150 620 1245 680 V880 C1000 1020 700 1040 420 990 C250 960 100 930 0 915 Z" fill="var(--white)"/>

      <path role="img" aria-label="Photo: a masked therapist helping an older man lift a hand weight outdoors" d="M0 925 C150 945 300 970 430 1000 C620 1120 705 1350 680 1610 H0 Z" fill="url(#parkTones)"/>
      <path class="photo-edge" d="M430 1000 C620 1120 705 1350 680 1610" fill="none" stroke="var(--slate)" stroke-width="22"/>
    </svg>

    <div class="badge">Silver Aspen Care Center<br>Ridgeline, Nevada</div>

    <div class="title-main">THERAPY</div>
    <div class="title-sub">POSITIONS</div>
    <div class="title-org">Silver Aspen Care Center</div>

    <div class="rate rate--pt"><span class="rate-role">Physical therapist</span><span class="rate-pay">$30 hr</span></div>
    <div class="rate rate--ot"><span class="rate-role">Occupational therapist</span><span class="rate-pay">$40 hr</span></div>

    <section class="intro">
      <h2 class="intro-heading">We are seeking caring and<br>compassionate therapists to join our team</h2>
      <p class="intro-body">Silver Aspen Care Center is a Skilled Nursing Facility in Ridgeline, Nevada. At the heart of Aspen County, Ridgeline is a friendly, rural mountain town in Eastern Nevada that is rich with art and history, as well as an abundance of opportunities for outdoor adventure.</p>
    </section>
    <div class="intro-rule"></div>

    <section class="contact">
      <h3 class="contact-title">Recruiting Contact</h3>
      <div class="contact-line">Dana Morrow</div>
      <div class="contact-line">Director of Rehab</div>
      <div class="contact-row contact-phone">
        <span>555-014-2290 EXT. 1200</span>
        <svg width="20" height="20" viewBox="0 0 24 24" aria-hidden="true"><path d="M6.6 10.8c1.4 2.8 3.8 5.1 6.6 6.6l2.2-2.2c.3-.3.7-.4 1-.2 1.1.4 2.3.6 3.6.6.6 0 1 .4 1 1V20c0 .6-.4 1-1 1C10.6 21 3 13.4 3 4c0-.6.4-1 1-1h3.5c.6 0 1 .4 1 1 0 1.3.2 2.5.6 3.6.1.3 0 .7-.2 1z" fill="var(--white)"/></svg>
      </div>
      <div class="contact-row contact-email">
        <span>dmorrow@silveraspencare.com</span>
        <svg width="18" height="13" viewBox="0 0 18 13" aria-hidden="true"><rect x="0.75" y="0.75" width="16.5" height="11.5" fill="none" stroke="var(--white)" stroke-width="1.5"/><path d="M1 1 L9 7.5 L17 1" fill="none" stroke="var(--white)" stroke-width="1.5"/></svg>
      </div>
    </section>
  </main>
</body>
</html>
```